Business card design needed

Design:
Want the logo/design to have an enviromental feel
Simple look not to busy

Company Info:
Pre purchase building and pest inspections
Registered building practitoner DB-U 48157 (please include building commission logo in design)

Industry/Entity Type

Building

Contact Information for Business Card

Company name:
Fernway Building and Pest inspections

Inspectors:
Dean Parkes 0471 958 214
Jack Severn 0419 562 847
Email: fernbpi@mailbox-demo.net

```html
<!DOCTYPE html>
<html lang="en">
<head>
<meta charset="utf-8">
<title>Fernway Building and Pest Inspections – Business Card</title>
<link rel="stylesheet" href="https://fonts.googleapis.com/css2?family=Didact+Gothic&family=Tinos:ital@1&display=swap">
<style>
  :root {
    --backdrop: #e6e7e8;
    --card: #ffffff;
    --brand-blue: #4aa9c9;
    --brand-green: #4cb93b;
    --text-light: #ffffff;
    --shadow: rgba(0, 0, 0, 0.18);
  }
  * { margin: 0; padding: 0; box-sizing: border-box; }
  html, body {
    width: 1200px;
    height: 800px;
    overflow: hidden;
    background: var(--backdrop);
  }
  .stage {
    position: relative;
    width: 1200px;
    height: 800px;
    display: flex;
    align-items: center;
    justify-content: center;
  }
  .business-card {
    position: relative;
    width: 960px;
    height: 587px;
    background: var(--card);
    box-shadow: 0 10px 30px var(--shadow);
    overflow: hidden;
    font-family: "Didact Gothic", "Century Gothic", sans-serif;
  }
  .card-shapes {
    position: absolute;
    inset: 0;
    width: 100%;
    height: 100%;
  }
  .tagline {
    position: absolute;
    left: 118px;
    top: 196px;
    font-family: "Tinos", "Times New Roman", serif;
    font-style: italic;
    font-size: 31px;
    line-height: 1.3;
    color: var(--brand-green);
    text-align: center;
  }
  .wordmark {
    position: absolute;
    left: 520px;
    top: 110px;
    display: flex;
    align-items: center;
    gap: 18px;
  }
  .wordmark-dot {
    width: 26px;
    height: 26px;
    border-radius: 50%;
    background: var(--brand-green);
    flex: none;
  }
  .wordmark-name {
    font-family: "Didact Gothic", "Century Gothic", sans-serif;
    font-size: 40px;
    line-height: 1.15;
    color: var(--brand-green);
    letter-spacing: 0.5px;
  }
  .contacts {
    color: var(--text-light);
    font-size: 26px;
    letter-spacing: 0.5px;
  }
  .label { font-weight: 700; margin-right: 6px; }
  .inspectors-heading {
    position: absolute;
    right: 560px;
    top: 470px;
    text-align: right;
    font-size: 30px;
    letter-spacing: 1px;
  }
  .email {
    position: absolute;
    right: 548px;
    top: 512px;
    font-size: 25px;
  }
  .inspector {
    position: absolute;
    line-height: 1.3;
  }
  .inspector-name {
    font-size: 29px;
    letter-spacing: 1px;
    text-transform: uppercase;
  }
  .inspector-phone { font-size: 25px; }
  .inspector--first { left: 478px; top: 418px; }
  .inspector--second { left: 742px; top: 362px; }
  .inspector-divider {
    position: absolute;
    left: 720px;
    top: 380px;
    width: 1px;
    height: 70px;
    background: rgba(255, 255, 255, 0.6);
  }
</style>
</head>
<body>
<main class="stage">
  <article class="business-card">
    <svg class="card-shapes" viewBox="0 0 960 587" aria-hidden="true">
      <path class="accent-swoosh" fill="var(--brand-green)"
            d="M540 320 C 700 300, 860 280, 960 262 L 960 282 C 860 300, 700 318, 540 320 Z"/>
      <path class="contact-band" fill="var(--brand-blue)"
            d="M0 375 C 220 330, 380 300, 560 318 C 720 332, 860 300, 960 282 L 960 587 L 0 587 Z"/>
    </svg>

    <p class="tagline">Pre purchase building<br>and pest inspections</p>

    <div class="wordmark">
      <span class="wordmark-dot"></span>
      <span class="wordmark-name">Fernway Building<br>and Pest Inspections</span>
    </div>

    <section class="contacts">
      <p class="inspectors-heading">INSPECTORS:</p>
      <p class="email"><span class="label">E:</span>fernbpi@mailbox-demo.net</p>

      <div class="inspector inspector--first">
        <p class="inspector-name">Jack Severn</p>
        <p class="inspector-phone"><span class="label">T:</span>0419 562 847</p>
      </div>
      <span class="inspector-divider"></span>
      <div class="inspector inspector--second">
        <p class="inspector-name">Dean Parkes</p>
        <p class="inspector-phone"><span class="label">T:</span>0471 958 214</p>
      </div>
    </section>
  </article>
</main>
</body>
</html>
```